Business Card for beauty technology startup

Design Glowmi Business Card for a Beauty, based on the website identity and colors (https://www.glowmi-example.com).
Glowmi is a beauty tech startup that gathers helpful product info for beauty lovers and consumers (such as availability on stores, price range and product reviews) for makeup products. The card design must be young, colorful but clean, and very modern.

Target Market(s)

woman, 15-35

Industry/Entity Type

Cosmetics

Contact Information for Business Card

Full Name, address, phone

Font styles to use
Other font styles liked:
• Advent Pro

Colors
e34297
86cfc6
ffffff
5c5c5c
e8e8e8
e667a6
b2b2b2

Requirements
Must have
• One full colored side with a creative design and another with card info
• Use Color palette: #95C5C5 and/or #D38AA5
• Use fonts: Advent Pro
• Use website identity: https://www.glowmi-example.com
Nice to have
• If needed extra font: Roboto

```html
<!DOCTYPE html>
<html lang="en">
<head>
<meta charset="utf-8">
<title>Glowmi Business Card</title>
<link rel="stylesheet" href="https://fonts.googleapis.com/css2?family=Advent+Pro:wght@300;400;600&family=Barlow:wght@400&display=swap">
<style>
  :root {
    --backdrop: #e6e6e6;
    --card-top: #cc7f99;
    --card-bottom: #bd728c;
    --ink-dark: #2b2429;
    --ink-light: #ffffff;
    --ink-soft: rgba(255, 255, 255, 0.92);
  }
  * { margin: 0; padding: 0; box-sizing: border-box; }
  html, body {
    width: 1200px;
    height: 576px;
    overflow: hidden;
    background: var(--backdrop);
  }
  .canvas {
    position: relative;
    width: 1200px;
    height: 576px;
  }
  .card {
    position: absolute;
    top: 138px;
    width: 484px;
    height: 295px;
    border-radius: 13px;
    background: linear-gradient(180deg, var(--card-top) 0%, var(--card-bottom) 100%);
    box-shadow: 0 2px 5px rgba(0, 0, 0, 0.18);
    overflow: hidden;
  }
  .card--front { left: 82px; }
  .card--back { left: 602px; width: 481px; height: 292px; }

  .brand {
    position: absolute;
    display: flex;
    align-items: center;
    font-family: "Advent Pro", sans-serif;
    font-weight: 300;
    text-transform: uppercase;
    line-height: 1;
  }
  .brand__dot {
    flex: none;
    border-radius: 50%;
    border-style: solid;
  }
  .brand--front {
    left: 104px;
    top: 120px;
    color: var(--ink-dark);
    font-size: 48px;
    letter-spacing: 5px;
  }
  .brand--front .brand__dot {
    width: 54px;
    height: 54px;
    border-width: 1.6px;
    border-color: var(--ink-dark);
    margin-right: 40px;
  }
  .brand--back {
    right: 28px;
    top: 40px;
    color: var(--ink-light);
    font-size: 36px;
    letter-spacing: 4px;
  }
  .brand--back .brand__dot {
    width: 36px;
    height: 36px;
    border-width: 1.4px;
    border-color: var(--ink-light);
    margin-right: 18px;
  }

  .holder {
    position: absolute;
    left: 24px;
    top: 203px;
    font-family: "Advent Pro", sans-serif;
    font-weight: 600;
    font-size: 23px;
    letter-spacing: 0.5px;
    color: var(--ink-light);
    text-transform: uppercase;
    line-height: 1;
  }
  .contact-list {
    position: absolute;
    left: 24px;
    top: 197px;
    list-style: none;
    font-family: "Barlow", sans-serif;
    font-size: 12.5px;
    color: var(--ink-soft);
  }
  .contact-list__item {
    display: flex;
    align-items: center;
    height: 16.5px;
  }
  .contact-list__icon {
    width: 11px;
    height: 11px;
    margin-right: 11px;
    fill: none;
    stroke: var(--ink-light);
    stroke-width: 1.3;
    stroke-linecap: round;
    stroke-linejoin: round;
  }
  .address {
    position: absolute;
    left: 24px;
    top: 252px;
    font-family: "Barlow", sans-serif;
    font-size: 12.5px;
    color: var(--ink-soft);
  }
</style>
</head>
<body>
<main class="canvas">
  <section class="card card--front" aria-label="Card front">
    <div class="brand brand--front">
      <span class="brand__dot"></span>
      <span class="brand__name">Glowmi</span>
    </div>
  </section>

  <section class="card card--back" aria-label="Card back">
    <div class="brand brand--back">
      <span class="brand__dot"></span>
      <span class="brand__name">Glowmi</span>
    </div>

    <h1 class="holder" style="top:170px">Mara Lind</h1>

    <ul class="contact-list">
      <li class="contact-list__item">
        <svg class="contact-list__icon" viewBox="0 0 12 12" aria-hidden="true">
          <path d="M2.5 1.2 L4.3 1.2 L5 3.6 L3.8 4.6 C4.5 6 5.8 7.4 7.4 8.2 L8.4 7 L10.8 7.7 L10.8 9.5 C10.8 10.3 10.1 10.9 9.3 10.8 C5 10.3 1.7 7 1.2 2.7 C1.1 1.9 1.7 1.2 2.5 1.2 Z"/>
        </svg>
        <span>00 555 010 202</span>
      </li>
      <li class="contact-list__item">
        <svg class="contact-list__icon" viewBox="0 0 12 12" aria-hidden="true">
          <path d="M5 7 L7 5"/>
          <path d="M6.2 3.2 L7.4 2 C8.2 1.2 9.6 1.2 10.2 1.8 C10.8 2.4 10.8 3.8 10 4.6 L8.8 5.8"/>
          <path d="M5.8 8.8 L4.6 10 C3.8 10.8 2.4 10.8 1.8 10.2 C1.2 9.6 1.2 8.2 2 7.4 L3.2 6.2"/>
        </svg>
        <span>www.glowmi-example.com</span>
      </li>
      <li class="contact-list__item">
        <svg class="contact-list__icon" viewBox="0 0 12 12" aria-hidden="true">
          <rect x="1" y="2.5" width="10" height="7" rx="0.6"/>
          <path d="M1.2 2.8 L6 6.6 L10.8 2.8"/>
        </svg>
        <span>yourname@glowmi-example.com</span>
      </li>
    </ul>

    <p class="address">123, Street Number, City Name, Country - 123456</p>
  </section>
</main>
</body>
</html>
```